Redesign the content on our home page

Thanks for your designs thus far.

There have been a few requests for feedback, so I have mocked up another layout. I am happy with everything except the 6 boxes in the green square. This is the piece I need the perfect design for.
- What the boxes look like
- Icons to be used
- Colours
- etc

__________________________________________________________________

We have the basic layout for our homepage, the header and footer are done. Please see attached (Homepage)

Only design in PSD etc needed, no coding. Also, header and footer not needed either, only formatting and graphic design of home page content. See eps file for the information.

I need more information added to the homepage and displayed in an organised way and designed so it presents well.

Our slogan is "Travel Insurance made simple". Therefore the design needs to represent this by being a simple, clear and clean layout of information. Website visitors need to be able to access and digest the information fast and this is reliant on the design of the information.

Attached is a mock up with all of the information.

Please ask and questions you need to help with the design.

Project Deadline Extended Reason: Deadline has been extended to provide further clarification for the required design.I need the 6 boxes inside the green outline designed. The design of the 6 boxes should be simple and follow the pages design and be simple in appearance. Thanks for your designs thus far. Added Thursday, October 8, 2015

Target Market(s)

Mostly female, any age.

Industry/Entity Type

Travel

Number of Pages Required

1 page

Font styles to use
Other font styles liked:
• MetaPro

Colors
f37122
33a6d7
33b8a4
dbdbdb
606060

Requirements
Must have
• - Follow home page look and feel
• - Simple design
• - Fast for a visitor to digest the information
Nice to have
• Simple design. Webpage is responsive so elements should look good when scaled for mobile.
Should not have
• No new colours to be introduced then what is in the design already or selected below.
• No new fonts.

```html
<!DOCTYPE html>
<html lang="en">
<head>
<meta charset="utf-8">
<title>wandercare – Travel Insurance made simple</title>
<link href="https://fonts.googleapis.com/css2?family=Fira+Sans:wght@300;400;500;700&display=swap" rel="stylesheet">
<style>
:root{
  --orange:#f37122;
  --orange-soft:#fbd9c2;
  --blue:#33a6d7;
  --teal:#33b8a4;
  --light:#dbdbdb;
  --grey:#606060;
  --dark:#2e2e2e;
  --ink:#1f1f1f;
  --white:#ffffff;
}
*{box-sizing:border-box;margin:0;padding:0}
html,body{width:778px;height:1200px;overflow:hidden}
body{font-family:"Fira Sans",Arial,sans-serif;color:var(--grey);background:var(--white);position:relative}

.site-header{position:absolute;top:0;left:0;width:778px;height:50px;background:rgba(255,255,255,.97);display:flex;align-items:center;padding:0 14px 0 18px;z-index:3}
.brand{display:flex;flex-direction:column;line-height:1}
.brand-name{font-size:24px;font-weight:700;color:var(--orange);white-space:nowrap}
.brand-tag{font-size:8px;color:var(--grey);margin-top:3px;white-space:nowrap}
.main-nav{display:flex;margin-left:40px;height:50px}
.main-nav a{display:flex;align-items:center;padding:0 16px;font-size:8.5px;font-weight:500;color:var(--grey);text-decoration:none;letter-spacing:.4px;white-space:nowrap}
.main-nav a.active{background:var(--orange);color:var(--white)}
.header-call{margin-left:auto;display:flex;align-items:center;gap:6px}
.call-icon{width:22px;height:22px;border-radius:50%;background:var(--orange);display:flex;align-items:center;justify-content:center}
.call-text{font-size:8px;line-height:1.3;color:var(--grey);white-space:nowrap}
.call-text strong{display:block;font-size:10px;color:var(--orange)}

.hero{position:absolute;top:0;left:0;width:778px;height:600px;background:linear-gradient(180deg,#8d9199 0%,#6e6a66 40%,#4a4542 75%,#3a3634 100%)}
.quote-box{position:absolute;top:60px;left:505px;width:210px;background:rgba(40,40,40,.85);z-index:2}
.quote-head{background:var(--orange);color:var(--white);font-size:10px;font-weight:500;text-align:center;padding:8px 10px;line-height:1.3}
.quote-body{padding:10px 12px 12px}
.field-label{font-size:8px;color:var(--light);margin-bottom:3px;white-space:nowrap}
.field{height:16px;background:var(--white);margin-bottom:8px}
.date-row{display:flex;gap:6px;align-items:center;margin-bottom:6px}
.date-row .field-label{width:26px;margin:0}
.date-row .field{flex:1;margin:0}
.date-btn{width:16px;height:16px;background:var(--orange)}
.quote-btn{margin-top:8px;height:22px;background:var(--orange);color:var(--white);font-size:9px;font-weight:500;display:flex;align-items:center;justify-content:center}

.why{position:absolute;top:345px;left:0;width:778px;text-align:center;z-index:2}
.why h2{font-size:22px;font-weight:400;color:var(--white)}
.why-grid{display:flex;justify-content:center;gap:14px;margin-top:26px}
.why-item{width:164px;display:flex;flex-direction:column;align-items:center}
.why-icon{width:72px;height:72px;border-radius:50%;background:var(--orange);border:3px solid rgba(255,255,255,.85);display:flex;align-items:center;justify-content:center}
.why-item h3{font-size:10px;font-weight:500;color:var(--orange);margin-top:10px;letter-spacing:.5px;white-space:nowrap}
.why-item p{font-size:7.5px;line-height:1.45;color:var(--white);margin-top:5px}
.why-item .more{font-size:7.5px;color:var(--orange);margin-top:4px}

.newsletter{position:absolute;top:600px;left:0;width:778px;height:150px;background:var(--orange);text-align:center}
.newsletter h2{font-size:22px;font-weight:400;color:var(--white);margin-top:34px}
.news-form{display:flex;justify-content:center;gap:12px;margin-top:26px}
.news-input{width:250px;height:30px;background:var(--orange-soft);font-size:9px;color:var(--grey);text-align:left;padding:10px}
.news-btn{width:180px;height:30px;background:var(--dark);color:var(--white);font-size:11px;font-weight:500;display:flex;align-items:center;justify-content:center;letter-spacing:1px}

.service{position:absolute;top:750px;left:0;width:778px;height:390px;background:linear-gradient(180deg,#5a4a3c 0%,#3e342c 100%)}
.service h2{font-size:24px;font-weight:400;color:var(--white);text-align:center;margin-top:28px}
.service h2 span{color:var(--orange)}
.service-intro{font-size:7.5px;line-height:1.5;color:var(--light);width:660px;margin:10px auto 0;text-align:center}
.cards{display:flex;justify-content:center;gap:14px;margin-top:20px}
.card{width:218px}
.card-photo{height:118px}
.card h3{font-size:8.5px;font-weight:500;color:var(--orange);margin-top:8px;white-space:nowrap}
.card p{font-size:7.5px;line-height:1.45;color:var(--light);margin-top:4px}
.card-btn{display:inline-block;margin-top:8px;background:var(--dark);color:var(--white);font-size:8px;padding:5px 10px}

.site-footer{position:absolute;top:1140px;left:0;width:778px;height:60px;background:var(--ink);display:flex;flex-direction:column;align-items:center;justify-content:center;gap:6px}
.foot-links{font-size:8px;color:var(--light)}
.foot-links span{margin:0 4px}
.foot-copy{font-size:7px;color:#9a9a9a}
.socials{position:absolute;right:22px;top:22px;display:flex;gap:8px}
.socials i{width:12px;height:12px;border-radius:50%;background:var(--grey);display:block}
</style>
</head>
<body>

<div class="hero" role="img" aria-label="Couple taking a selfie in front of the Eiffel Tower in Paris"></div>

<header class="site-header">
  <div class="brand">
    <span class="brand-name">wandercare</span>
    <span class="brand-tag">Travel Insurance made simple</span>
  </div>
  <nav class="main-nav">
    <a class="active">TRAVEL INSURANCE</a>
    <a>WHAT WE COVER</a>
    <a>YOUR POLICY</a>
    <a>FAQ</a>
    <a>EMERGENCY</a>
  </nav>
  <div class="header-call">
    <span class="call-icon"><svg width="11" height="11" viewBox="0 0 24 24"><path fill="#fff" d="M6.6 10.8a15 15 0 0 0 6.6 6.6l2.2-2.2c.3-.3.7-.4 1-.2 1.1.4 2.3.6 3.6.6.6 0 1 .4 1 1V20c0 .6-.4 1-1 1A17 17 0 0 1 3 4c0-.6.4-1 1-1h3.5c.6 0 1 .4 1 1 0 1.3.2 2.5.6 3.6.1.3 0 .7-.2 1z"/></svg></span>
    <span class="call-text">Call us<strong>1800 555 210</strong></span>
  </div>
</header>

<aside class="quote-box">
  <div class="quote-head">Start Getting Your Travel Insurance Quote Now!</div>
  <div class="quote-body">
    <div class="field-label">I am Travelling to</div>
    <div class="field"></div>
    <div class="date-row"><span class="field-label">From</span><span class="field"></span><span class="field-label">Dep</span><span class="field"></span></div>
    <div class="date-row"><span class="field-label">Age</span><span class="date-btn"></span><span class="field"></span></div>
    <div class="quote-btn">SEARCH</div>
  </div>
</aside>

<section class="why">
  <h2>Why Choose wandercare?</h2>
  <div class="why-grid">
    <div class="why-item">
      <div class="why-icon"><svg width="32" height="32" viewBox="0 0 32 32"><rect x="5" y="17" width="5" height="10" fill="#fff"/><rect x="13.5" y="11" width="5" height="16" fill="#fff"/><rect x="22" y="6" width="5" height="21" fill="#fff"/></svg></div>
      <h3>TRUSTED INSURER</h3>
      <p>Your policy is backed by a leading global insurer with decades of travel cover experience.</p>
      <span class="more">Read More »</span>
    </div>
    <div class="why-item">
      <div class="why-icon"><svg width="32" height="32" viewBox="0 0 32 32" fill="none" stroke="#fff" stroke-width="2.5"><path d="M9 5v9a6 6 0 0 0 12 0V5"/><path d="M15 20v3a5 5 0 0 0 10 0v-3"/><circle cx="25" cy="17" r="3"/></svg></div>
      <h3>MEDICAL CONDITIONS</h3>
      <p>Many existing medical conditions are covered automatically with no extra forms needed.</p>
      <span class="more">Read More »</span>
    </div>
    <div class="why-item">
      <div class="why-icon"><svg width="32" height="32" viewBox="0 0 32 32" fill="none" stroke="#fff" stroke-width="2.5"><circle cx="16" cy="16" r="11"/><path d="M16 9v7l5 3"/></svg></div>
      <h3>IMMEDIATE COVER</h3>
      <p>Buy online in minutes and your policy documents arrive instantly by email.</p>
      <span class="more">Read More »</span>
    </div>
    <div class="why-item">
      <div class="why-icon"><svg width="32" height="32" viewBox="0 0 32 32"><rect x="13" y="5" width="6" height="22" fill="#fff"/><rect x="5" y="13" width="22" height="6" fill="#fff"/></svg></div>
      <h3>EMERGENCY</h3>
      <p>Our assistance team is ready to help you anywhere in the world, day or night.</p>
      <span class="more">Read More »</span>
    </div>
  </div>
</section>

<section class="newsletter">
  <h2>Want travel tips &amp; freebies?&nbsp; Join our newsletter!</h2>
  <div class="news-form">
    <div class="news-input">Enter Your Name</div>
    <div class="news-input">Enter Your Email</div>
    <div class="news-btn">SIGN UP</div>
  </div>
</section>

<section class="service">
  <h2>Our <span>Service</span></h2>
  <p class="service-intro">We make travel insurance simple, with clear cover options, fair prices and friendly support before, during and after your trip. Compare plans, choose the cover that suits your journey and travel with peace of mind wherever you go.</p>
  <div class="cards">
    <article class="card">
      <div class="card-photo" role="img" aria-label="Statue of Liberty under a blue sky" style="background:linear-gradient(180deg,#5fa8d8,#3b7f8a 70%,#4a6a3a)"></div>
      <h3>TOP TRAVEL DESTINATIONS THIS YEAR</h3>
      <p>See where travellers are heading and what cover you need for each place.</p>
      <span class="card-btn">READ MORE</span>
    </article>
    <article class="card">
      <div class="card-photo" role="img" aria-label="Family walking together on a sunny beach" style="background:linear-gradient(180deg,#8cc8e8,#cfe4ea 55%,#e8d8b8)"></div>
      <h3>FAMILY TRAVEL TIPS FOR A HOLIDAY</h3>
      <p>Simple ideas to keep the whole family safe, happy and covered on holiday.</p>
      <span class="card-btn">READ MORE</span>
    </article>
    <article class="card">
      <div class="card-photo" role="img" aria-label="Traveller relaxing in a deck chair by the sea" style="background:linear-gradient(180deg,#6fc0e0,#4aa8c8 55%,#e4cfa6)"></div>
      <h3>SMART WAYS TO SAVE WHILE OVERSEAS</h3>
      <p>Easy money tips to help your travel budget go further on every trip.</p>
      <span class="card-btn">READ MORE</span>
    </article>
  </div>
</section>

<footer class="site-footer">
  <div class="foot-links"><span>Home</span>|<span>About Us</span>|<span>Our Service</span>|<span>Testimonials</span>|<span>Contact</span>|<span>Sitemap</span></div>
  <div class="foot-copy">© wandercare. All rights reserved.</div>
  <div class="socials"><i></i><i></i><i></i><i></i><i></i></div>
</footer>

</body>
</html>
```